Copper Lantern Coffee Bean Labels

We need a label for a new brand of coffee that we are selling in Portland, Oregon (Coffee Capital). Our company has no current online presence but have some great roasting techniques. We will be roasting our own coffee beans from throughout the world and selling them immediately after roasting causing a super fresh and high quality product.

We will be packaging in brown kraft bags: 3 3/8 X 2.5 x 7.75 inches which is standard for coffee beans.

Also notice on that sample the blue section in the middle has the product name. We want to also make it so that there is a consistent area that we can print OVER the label the name or blend of the coffee.

Our company is called Copper Lantern Coffee Roasters. We will want to put copperlanternroasters.example on the label someplace (we dont have a site yet but will by launch).

We need to incorporate A Black Diamond into the design. No preferences yet on the style of it.

We want to be a super-premium brand. Sort of like MicroBrew beers. We will sell at Farmers Markets, online, and directly into stores. Image is very important to us.

Labels should be about 3" wide and about 3.75" high.. Perhaps higher if a cool design justifies the height. Again we will be using a brown kraft bag (like grocery bag color) as shown on the sample.

SEE ATTACHED SEVERAL INTERESTING DESIGNS

Target Market(s)

Foodies, Yuppie, Coffee Snob

Industry/Entity Type

It Company

Requirements
Must have
• Location for the product Name to go onto it... We want to use the same labels for our full line. Just printing over it something like "Italian Roast" and a line below saying something like "Bold, Nutty Flavor, blah blah"

Should not have
• Clunkey looking old fonts or things that look homemade.

```html
<!DOCTYPE html>
<html lang="en">
<head>
<meta charset="utf-8">
<title>Copper Lantern Coffee Bean Labels</title>
<link rel="stylesheet" href="https://fonts.googleapis.com/css2?family=Arimo&family=Josefin+Sans:wght@700&display=swap">
<style>
  :root {
    --paper: #ffffff;
    --blush: #f5b9ca;
    --mint: #8fd3c1;
    --ink: #1c1c1c;
  }
  html, body {
    margin: 0;
    padding: 0;
    width: 1200px;
    height: 1200px;
    overflow: hidden;
    background: var(--paper);
  }
  .label-sheet { display: block; width: 1200px; height: 1200px; }
  .edge-blush { fill: var(--blush); }
  .edge-mint { fill: var(--mint); }
  .edge-paper { fill: var(--paper); }
  .blend-line {
    font-family: "Arimo", Arial, sans-serif;
    font-size: 17px;
    fill: var(--paper);
    letter-spacing: 0.02em;
  }
  .web-line {
    font-family: "Arimo", Arial, sans-serif;
    font-size: 12.5px;
    letter-spacing: 0.01em;
  }
  .web-line--mint { fill: var(--mint); }
  .web-line--blush { fill: var(--blush); }
  .brand-name {
    font-family: "Josefin Sans", "Helvetica Neue", sans-serif;
    font-weight: 700;
    fill: var(--ink);
    text-anchor: middle;
  }
  .brand-name--main { font-size: 25px; letter-spacing: 0.26em; }
  .brand-name--sub { font-size: 14px; letter-spacing: 0.14em; }
  .side-dot { fill: none; stroke: var(--paper); stroke-width: 1.6; }
</style>
</head>
<body>
<svg class="label-sheet" viewBox="0 0 1200 1200" xmlns="http://www.w3.org/2000/svg">
  <defs>
    <g id="serrated-disc">
      <polygon points="0,0 -7.45,-94.7 0,-100 7.45,-94.7" transform="rotate(0)"/>
      <polygon points="0,0 -7.45,-94.7 0,-100 7.45,-94.7" transform="rotate(9)"/>
      <polygon points="0,0 -7.45,-94.7 0,-100 7.45,-94.7" transform="rotate(18)"/>
      <polygon points="0,0 -7.45,-94.7 0,-100 7.45,-94.7" transform="rotate(27)"/>
      <polygon points="0,0 -7.45,-94.7 0,-100 7.45,-94.7" transform="rotate(36)"/>
      <polygon points="0,0 -7.45,-94.7 0,-100 7.45,-94.7" transform="rotate(45)"/>
      <polygon points="0,0 -7.45,-94.7 0,-100 7.45,-94.7" transform="rotate(54)"/>
      <polygon points="0,0 -7.45,-94.7 0,-100 7.45,-94.7" transform="rotate(63)"/>
      <polygon points="0,0 -7.45,-94.7 0,-100 7.45,-94.7" transform="rotate(72)"/>
      <polygon points="0,0 -7.45,-94.7 0,-100 7.45,-94.7" transform="rotate(81)"/>
      <polygon points="0,0 -7.45,-94.7 0,-100 7.45,-94.7" transform="rotate(90)"/>
      <polygon points="0,0 -7.45,-94.7 0,-100 7.45,-94.7" transform="rotate(99)"/>
      <polygon points="0,0 -7.45,-94.7 0,-100 7.45,-94.7" transform="rotate(108)"/>
      <polygon points="0,0 -7.45,-94.7 0,-100 7.45,-94.7" transform="rotate(117)"/>
      <polygon points="0,0 -7.45,-94.7 0,-100 7.45,-94.7" transform="rotate(126)"/>
      <polygon points="0,0 -7.45,-94.7 0,-100 7.45,-94.7" transform="rotate(135)"/>
      <polygon points="0,0 -7.45,-94.7 0,-100 7.45,-94.7" transform="rotate(144)"/>
      <polygon points="0,0 -7.45,-94.7 0,-100 7.45,-94.7" transform="rotate(153)"/>
      <polygon points="0,0 -7.45,-94.7 0,-100 7.45,-94.7" transform="rotate(162)"/>
      <polygon points="0,0 -7.45,-94.7 0,-100 7.45,-94.7" transform="rotate(171)"/>
      <polygon points="0,0 -7.45,-94.7 0,-100 7.45,-94.7" transform="rotate(180)"/>
      <polygon points="0,0 -7.45,-94.7 0,-100 7.45,-94.7" transform="rotate(189)"/>
      <polygon points="0,0 -7.45,-94.7 0,-100 7.45,-94.7" transform="rotate(198)"/>
      <polygon points="0,0 -7.45,-94.7 0,-100 7.45,-94.7" transform="rotate(207)"/>
      <polygon points="0,0 -7.45,-94.7 0,-100 7.45,-94.7" transform="rotate(216)"/>
      <polygon points="0,0 -7.45,-94.7 0,-100 7.45,-94.7" transform="rotate(225)"/>
      <polygon points="0,0 -7.45,-94.7 0,-100 7.45,-94.7" transform="rotate(234)"/>
      <polygon points="0,0 -7.45,-94.7 0,-100 7.45,-94.7" transform="rotate(243)"/>
      <polygon points="0,0 -7.45,-94.7 0,-100 7.45,-94.7" transform="rotate(252)"/>
      <polygon points="0,0 -7.45,-94.7 0,-100 7.45,-94.7" transform="rotate(261)"/>
      <polygon points="0,0 -7.45,-94.7 0,-100 7.45,-94.7" transform="rotate(270)"/>
      <polygon points="0,0 -7.45,-94.7 0,-100 7.45,-94.7" transform="rotate(279)"/>
      <polygon points="0,0 -7.45,-94.7 0,-100 7.45,-94.7" transform="rotate(288)"/>
      <polygon points="0,0 -7.45,-94.7 0,-100 7.45,-94.7" transform="rotate(297)"/>
      <polygon points="0,0 -7.45,-94.7 0,-100 7.45,-94.7" transform="rotate(306)"/>
      <polygon points="0,0 -7.45,-94.7 0,-100 7.45,-94.7" transform="rotate(315)"/>
      <polygon points="0,0 -7.45,-94.7 0,-100 7.45,-94.7" transform="rotate(324)"/>
      <polygon points="0,0 -7.45,-94.7 0,-100 7.45,-94.7" transform="rotate(333)"/>
      <polygon points="0,0 -7.45,-94.7 0,-100 7.45,-94.7" transform="rotate(342)"/>
      <polygon points="0,0 -7.45,-94.7 0,-100 7.45,-94.7" transform="rotate(351)"/>
    </g>
    <path id="blend-arc-top" d="M -178,0 A 178 178 0 0 1 178,0"/>
    <path id="blend-arc-bottom" d="M -194,0 A 194 194 0 0 0 194,0"/>
    <path id="web-arc-top" d="M -126,0 A 126 126 0 0 1 126,0"/>
    <path id="web-arc-bottom" d="M -137,0 A 137 137 0 0 0 137,0"/>
  </defs>

  <!-- Blush label -->
  <g class="badge badge--blush" transform="translate(294 578)">
    <use href="#serrated-disc" class="edge-blush" transform="scale(2.22)"/>
    <use href="#serrated-disc" class="edge-paper" transform="scale(2.12)"/>
    <use href="#serrated-disc" class="edge-blush" transform="scale(2.06)"/>
    <use href="#serrated-disc" class="edge-paper" transform="scale(1.62)"/>
    <use href="#serrated-disc" class="edge-blush" transform="scale(1.57)"/>
    <use href="#serrated-disc" class="edge-paper" transform="scale(1.52)"/>

    <text class="blend-line"><textPath href="#blend-arc-top" startOffset="50%" text-anchor="middle">write blend here write blend here</textPath></text>
    <text class="blend-line"><textPath href="#blend-arc-bottom" startOffset="50%" text-anchor="middle">blend goes here&#160;&#160;&#160; blend goes here</textPath></text>

    <circle class="side-dot" cx="-184" cy="0" r="9"/>
    <circle class="side-dot" cx="184" cy="0" r="9"/>

    <text class="web-line web-line--mint"><textPath href="#web-arc-top" startOffset="50%" text-anchor="middle">copperlanternroasters.example</textPath></text>
    <text class="web-line web-line--mint"><textPath href="#web-arc-bottom" startOffset="50%" text-anchor="middle">copperlanternroasters.example</textPath></text>

    <text class="brand-name brand-name--main" x="6" y="-16">COPPER</text>
    <text class="brand-name brand-name--main" x="6" y="16">LANTERN</text>
    <text class="brand-name brand-name--sub" x="2" y="42">COFFEE ROASTERS</text>
  </g>

  <!-- Mint label -->
  <g class="badge badge--mint" transform="translate(866 586)">
    <use href="#serrated-disc" class="edge-mint" transform="scale(2.22)"/>
    <use href="#serrated-disc" class="edge-paper" transform="scale(2.12)"/>
    <use href="#serrated-disc" class="edge-mint" transform="scale(2.06)"/>
    <use href="#serrated-disc" class="edge-paper" transform="scale(1.62)"/>
    <use href="#serrated-disc" class="edge-mint" transform="scale(1.57)"/>
    <use href="#serrated-disc" class="edge-paper" transform="scale(1.52)"/>

    <text class="blend-line"><textPath href="#blend-arc-top" startOffset="50%" text-anchor="middle">write blend here write blend here</textPath></text>
    <text class="blend-line"><textPath href="#blend-arc-bottom" startOffset="50%" text-anchor="middle">write blend here write blend here</textPath></text>

    <circle class="side-dot" cx="-184" cy="0" r="9"/>
    <circle class="side-dot" cx="184" cy="0" r="9"/>

    <text class="web-line web-line--blush"><textPath href="#web-arc-top" startOffset="50%" text-anchor="middle">copperlanternroasters.example</textPath></text>
    <text class="web-line web-line--blush"><textPath href="#web-arc-bottom" startOffset="50%" text-anchor="middle">copperlanternroasters.example</textPath></text>

    <text class="brand-name brand-name--main" x="6" y="-16">COPPER</text>
    <text class="brand-name brand-name--main" x="6" y="16">LANTERN</text>
    <text class="brand-name brand-name--sub" x="2" y="42">COFFEE ROASTERS</text>
  </g>
</svg>
</body>
</html>
```